New Food Retail Product: 100% Quinoa Pasta

Do you enjoy eating food?

We need a packaging design completed for a new product which is a 100% Quinoa Pasta originating from Peru in Latin American. I currently do not have a name for this product and I am open to suggestions. For pasta design ideas please search "pasta packaging designs" in snapmural for ideas.My product is Gluteen free, has a high level of protein and does not contain any GMOs - the package design needs to fit 8oz or 227grams of pasta. As per the colours and design I am open to your ideas as I will know the one once it has been created for me.

Target Market(s)

Diabetes, Athletes, Millennials, Generation X, Individuals will high blood pressure
Gluten Free dieters, Vegans

Industry/Entity Type

Retail

Font styles to use
Sans Serif

Colors
33b8a4
3277b5
acd036
fbee3e
ec1f27

Requirements
Must have
• Clean upscale design as the product is a premium priced product
• For this project the designs required are for the following types of pasta: Fusilli and Linguine. As far as a picture the product looks lIke brown while wheat pasta.

```html
<!DOCTYPE html>
<html lang="en">
<head>
<meta charset="utf-8">
<title>Quorvinta Quinoa Pasta Packaging</title>
<link rel="stylesheet" href="https://fonts.googleapis.com/css2?family=Fredoka:wght@600&family=Oswald:wght@600&family=Roboto:wght@700;900&family=Ubuntu:wght@500&display=swap">
<style>
  :root{
    --bg:#e6eaec;
    --blue:#0f5fb0;
    --blue-deep:#0a4a92;
    --teal:#33b8a4;
    --green:#acd036;
    --yellow:#fbee3e;
    --red:#ec1f27;
    --white:#ffffff;
    --pasta-light:#f3d27a;
    --pasta-dark:#c9922e;
  }
  *{margin:0;padding:0;box-sizing:border-box}
  html,body{width:1007px;height:1200px;overflow:hidden;background:var(--bg)}
  .canvas{position:relative;width:1007px;height:1200px}
  .pack{position:absolute;background:var(--blue);overflow:hidden;text-align:center}
  .pack--fusilli{left:168px;top:397px;width:336px;height:607px}
  .pack--linguine{left:552px;top:71px;width:289px;height:1069px}
  .pack__art{position:absolute;inset:0;width:100%;height:100%}
  .pack__text{position:absolute;left:0;right:0;white-space:nowrap}
  .brand{font-family:"Oswald",sans-serif;font-weight:600;color:var(--red);letter-spacing:.5px;line-height:1.2}
  .badge{position:absolute;left:50%;transform:translateX(-50%);background:var(--teal);color:var(--white);
    font-family:"Oswald",sans-serif;font-weight:600;white-space:nowrap;line-height:1.2;
    clip-path:polygon(0 0,100% 0,94% 100%,6% 100%)}
  .mascot{position:absolute;left:50%;transform:translateX(-50%);background:var(--red);border-radius:6px}
  .percent{font-family:"Fredoka",sans-serif;font-weight:600;color:var(--yellow);-webkit-text-stroke:2px var(--red);line-height:1}
  .grain{font-family:"Fredoka",sans-serif;font-weight:600;color:var(--red);-webkit-text-stroke:2px var(--white);line-height:1;letter-spacing:1px}
  .tagline{font-family:"Roboto",sans-serif;font-weight:700;color:var(--white)}
  .variety{font-family:"Ubuntu",sans-serif;font-weight:500;color:var(--green);line-height:1.1}
  .claim{position:absolute;font-family:"Roboto",sans-serif;font-weight:900;color:var(--yellow);line-height:1.05;text-align:left}
  .weight{position:absolute;font-family:"Roboto",sans-serif;font-weight:700;color:var(--yellow);white-space:nowrap;line-height:1.2}
</style>
</head>
<body>
<main class="canvas">

  <section class="pack pack--fusilli" aria-label="Fusilli pack front">
    <svg class="pack__art" viewBox="0 0 336 607" preserveAspectRatio="none">
      <defs>
        <linearGradient id="pastaFusilli" x1="0" y1="0" x2="1" y2="1">
          <stop offset="0" stop-color="var(--pasta-light)"/><stop offset="1" stop-color="var(--pasta-dark)"/>
        </linearGradient>
      </defs>
      <g role="img" aria-label="Fusilli pasta seen through the window">
        <polygon points="0,60 18,60 78,340 22,490 0,490" fill="url(#pastaFusilli)"/>
        <polygon points="336,60 318,60 258,340 314,490 336,490" fill="url(#pastaFusilli)"/>
      </g>
      <polygon points="68,0 271,0 170,200" fill="var(--green)"/>
      <g stroke="var(--red)" stroke-width="3" fill="none">
        <line x1="0" y1="110" x2="90" y2="500"/><line x1="336" y1="110" x2="246" y2="500"/>
      </g>
      <g stroke="var(--green)" stroke-width="2" fill="none">
        <line x1="22" y1="60" x2="120" y2="560"/><line x1="314" y1="60" x2="216" y2="560"/>
      </g>
    </svg>
    <div class="pack__text brand" style="top:68px;font-size:30px">QUORVINTA</div>
    <div class="badge" style="top:156px;font-size:20px;padding:4px 26px">GLUTEN-FREE</div>
    <div class="mascot" role="img" aria-label="Red llama illustration" style="top:192px;width:60px;height:57px"></div>
    <div class="pack__text percent" style="top:266px;font-size:44px">100%</div>
    <div class="pack__text grain" style="top:314px;font-size:68px">QUINOA</div>
    <div class="pack__text tagline" style="top:394px;font-size:22px;line-height:30px">Organic<br>Supergrain Pasta</div>
    <div class="pack__text variety" style="top:478px;font-size:24px">Fusilli</div>
    <div class="claim" style="left:42px;top:530px;font-size:15px">NON<br>GMO</div>
    <div class="weight" style="right:12px;top:553px;font-size:12px">NET WT. 8oz/227g</div>
  </section>

  <section class="pack pack--linguine" aria-label="Linguine pack front">
    <svg class="pack__art" viewBox="0 0 289 1069" preserveAspectRatio="none">
      <defs>
        <linearGradient id="pastaLinguine" x1="0" y1="0" x2="1" y2="0">
          <stop offset="0" stop-color="var(--pasta-dark)"/><stop offset=".5" stop-color="var(--pasta-light)"/><stop offset="1" stop-color="var(--pasta-dark)"/>
        </linearGradient>
      </defs>
      <rect x="0" y="0" width="289" height="14" fill="var(--blue-deep)"/>
      <rect x="0" y="1029" width="289" height="40" fill="var(--blue-deep)"/>
      <g role="img" aria-label="Linguine strands seen through the window">
        <polygon points="0,234 22,234 112,580 30,880 0,880" fill="url(#pastaLinguine)"/>
        <polygon points="289,234 267,234 177,580 259,880 289,880" fill="url(#pastaLinguine)"/>
      </g>
      <polygon points="26,14 263,14 145,286" fill="var(--green)"/>
      <g stroke="var(--red)" stroke-width="3" fill="none">
        <line x1="0" y1="280" x2="80" y2="860"/><line x1="289" y1="280" x2="209" y2="860"/>
      </g>
      <g stroke="var(--green)" stroke-width="2" fill="none">
        <line x1="22" y1="234" x2="140" y2="900"/><line x1="267" y1="234" x2="149" y2="900"/>
      </g>
    </svg>
    <div class="pack__text brand" style="top:120px;font-size:28px">QUORVINTA</div>
    <div class="badge" style="top:200px;font-size:20px;padding:4px 26px">GLUTEN-FREE</div>
    <div class="mascot" role="img" aria-label="Red llama illustration" style="top:339px;width:70px;height:73px"></div>
    <div class="pack__text percent" style="top:519px;font-size:44px">100%</div>
    <div class="pack__text grain" style="top:572px;font-size:60px">QUINOA</div>
    <div class="pack__text tagline" style="top:642px;font-size:21px;line-height:29px">Organic<br>Supergrain<br>Pasta</div>
    <div class="pack__text variety" style="top:814px;font-size:26px">Linguine</div>
    <div class="claim" style="left:45px;top:933px;font-size:15px">NON<br>GMO</div>
    <div class="weight" style="right:37px;top:952px;font-size:12px">NET WT. 8oz/227g</div>
  </section>

</main>
</body>
</html>
```